business card for dental office

We need a business card design for an existing company follwing information we need on the card:
Teodor L Vanwick, DDS
4263 Harlowe Court
Elmsworth, VA 20199
Ph: 703-555-0142 Fax:703-555-0187
www.grinvalemont.example info@grinvalemont.example
second side
Appointment
For
Date: day:
Time
if you are unable to keep your appointment, please contact us 24 hours in advance.
Note: Logo is attached to use with the card
Thanks
Industry/Entity Type
Dental Clinic
Contact Information for Business Card
Teodor L Vanwick, DDS
4263 Harlowe Court
Elmsworth, VA 20199
second side
Appointment
For
Date: day:
Time
Thanks

```html
<!DOCTYPE html>
<html lang="en">
<head>
<meta charset="utf-8">
<title>Grinvalemont Dental Associates – Business Card</title>
<link rel="stylesheet" href="https://fonts.googleapis.com/css2?family=Open+Sans:ital,wght@0,400;0,600;0,700;1,400&display=swap">
<style>
  :root {
    --navy: #0f4a7d;
    --cyan: #16b6e2;
    --brand: #1d5391;
    --paper: #ffffff;
    --ink: #5f6062;
    --rule: #9a9a9a;
    --label: #a3a3a3;
    --glow: #9fb6d8;
    --stage-light: #f7f7f7;
    --stage-mid: #ececec;
    --stage-dark: #d9d9d9;
  }
  * { box-sizing: border-box; margin: 0; padding: 0; }
  html, body { width: 1200px; height: 1000px; overflow: hidden; }
  body {
    position: relative;
    font-family: "Open Sans", Arial, sans-serif;
    background: radial-gradient(ellipse at 20% 25%, var(--stage-light) 0%, var(--stage-mid) 55%, var(--stage-dark) 100%);
  }
  .side-label {
    position: absolute;
    font-size: 30px;
    line-height: 41px;
    font-weight: 400;
    color: var(--label);
    letter-spacing: -0.3px;
  }
  .side-label--front { right: 875px; top: 162px; text-align: right; }
  .side-label--back { left: 849px; top: 764px; }

  .card {
    position: absolute;
    width: 762px;
    height: 434px;
    background: var(--paper);
    box-shadow: 6px 8px 14px rgba(0,0,0,0.28);
    overflow: hidden;
  }
  .card--front { left: 358px; top: 41px; }
  .card--back { left: 52px; top: 527px; }
  .card__art { position: absolute; inset: 0; width: 100%; height: 100%; }

  .card__url {
    position: absolute;
    left: 0; right: 0;
    text-align: center;
    color: var(--paper);
    font-weight: 700;
    font-size: 23px;
    letter-spacing: 10px;
    padding-left: 10px;
  }
  .card--front .card__url { top: 392px; }
  .card--back .card__url { top: 385px; }

  .brand {
    position: absolute;
    left: 0; right: 0;
    top: 146px;
    display: flex;
    align-items: center;
    justify-content: center;
    gap: 14px;
  }
  .brand__dot {
    width: 22px; height: 22px;
    border-radius: 50%;
    background: var(--cyan);
  }
  .brand__name {
    font-size: 34px;
    font-weight: 400;
    color: var(--brand);
    letter-spacing: 0.3px;
  }

  .contact {
    position: absolute;
    left: 0; right: 0;
    top: 261px;
    text-align: center;
    color: var(--ink);
    font-size: 18px;
    line-height: 27.5px;
    letter-spacing: 0.2px;
  }

  .appointment__title {
    position: absolute;
    left: 0; right: 0;
    top: 28px;
    text-align: center;
    font-size: 19px;
    font-weight: 700;
    letter-spacing: 3px;
    color: var(--ink);
  }
  .appointment__field {
    position: absolute;
    left: 80px;
    right: 71px;
    display: flex;
    align-items: flex-end;
    gap: 8px;
    font-size: 17px;
    color: var(--ink);
  }
  .appointment__field span { line-height: 20px; }
  .appointment__line {
    flex: 1;
    border-bottom: 1.5px solid var(--rule);
    margin-bottom: 4px;
  }
  .appointment__field--for { top: 98px; }
  .appointment__field--date { top: 159px; }
  .appointment__field--time { top: 220px; }
  .appointment__note {
    position: absolute;
    left: 0; right: 0;
    top: 267px;
    text-align: center;
    font-style: italic;
    font-size: 21px;
    line-height: 28px;
    letter-spacing: 0.3px;
    color: var(--ink);
  }
</style>
</head>
<body>

  <div class="side-label side-label--front">FRONT<br>BUSINESS CARD</div>
  <div class="side-label side-label--back">BACK<br>BUSINESS CARD</div>

  <section class="card card--front">
    <svg class="card__art" viewBox="0 0 762 434" aria-hidden="true">
      <defs>
        <filter id="glowFront" x="-10%" y="-50%" width="120%" height="200%">
          <feGaussianBlur stdDeviation="4"/>
        </filter>
      </defs>
      <path d="M0,0 H762 V86 Q381,-49 0,86 Z" fill="var(--navy)"/>
      <path d="M0,86 Q381,-49 762,86" fill="none" stroke="var(--glow)" stroke-width="10" filter="url(#glowFront)" opacity="0.8"/>
      <path d="M0,86 Q381,-49 762,86" fill="none" stroke="var(--cyan)" stroke-width="7"/>
      <path d="M0,316 Q381,405 762,316 V434 H0 Z" fill="var(--navy)"/>
      <path d="M0,316 Q381,405 762,316" fill="none" stroke="var(--glow)" stroke-width="12" filter="url(#glowFront)" opacity="0.8"/>
      <path d="M0,316 Q381,405 762,316" fill="none" stroke="var(--cyan)" stroke-width="7"/>
    </svg>

    <div class="brand">
      <span class="brand__dot"></span>
      <span class="brand__name">Grinvalemont Dental Associates</span>
    </div>

    <div class="contact">
      <p>Teodor L Vanwick, DDS, 4263 Harlowe Court, Elmsworth, VA 20199</p>
      <p>Ph: 703-555-0142 • Fax:703-555-0187</p>
      <p>info@grinvalemont.example</p>
    </div>

    <p class="card__url">WWW.GRINVALEMONT.EXAMPLE</p>
  </section>

  <section class="card card--back">
    <svg class="card__art" viewBox="0 0 762 434" aria-hidden="true">
      <defs>
        <filter id="glowBack" x="-10%" y="-50%" width="120%" height="200%">
          <feGaussianBlur stdDeviation="4"/>
        </filter>
      </defs>
      <path d="M0,298 Q381,420 762,288 V434 H0 Z" fill="var(--navy)"/>
      <path d="M0,298 Q381,420 762,288" fill="none" stroke="var(--glow)" stroke-width="12" filter="url(#glowBack)" opacity="0.8"/>
      <path d="M0,298 Q381,420 762,288" fill="none" stroke="var(--cyan)" stroke-width="7"/>
    </svg>

    <h2 class="appointment__title">APPOINTMENT</h2>
    <div class="appointment__field appointment__field--for"><span>For:</span><i class="appointment__line"></i></div>
    <div class="appointment__field appointment__field--date"><span>Date:</span><i class="appointment__line"></i></div>
    <div class="appointment__field appointment__field--time"><span>Time:</span><i class="appointment__line"></i></div>
    <p class="appointment__note">If you are unable to keep your appointment,<br>please contact us 24 hours in advance.</p>

    <p class="card__url">WWW.GRINVALEMONT.EXAMPLE</p>
  </section>

</body>
</html>
```